Wordpress Theme for Medical Clinics

** Please view updated Sitemap2.pdf doc to clarify some confusion ***

This is a multiuser WordPress subscription site for medical clinics. Please see attachment for sitemap. Please do not include extra content like social media icons, search bars, or images. If you have questions, please ask for clarification.
The site contains the following pages and sub-pages:

1. Home
2. Our Clinic
2a. Our Clinic > Mission
2b. Our Clinic > Services
2c. Our Clinic > Clinic Policies
2d. Our Clinic > Schedules
3. Our Staff
3a. Our Staff > [Staff member page]
4. Resources
4a. Resources > Patient Health (index)
4b. Resources > Patient Health (index) > [post]
4c. Resources > Links
4d. Resources > Forms
5. Alerts
5a. Alerts > [Alert Page]
6. Contact Us

Includes the Following Pages, Subpages, and Content
1. Home
a. About Us
b. Our Staff
c. Bulletins
d. Accepting New Patients (shown as an alert widget)
e. Links
i. Physician Toolbox
ii. Book an Appointment
f. Clinic Policies
i. Show first 3 policies (e.g. Late Arrivals, Missed Appointments, Fees)
ii. Link to Clinic Policies page
g. Primary widget (displayed on all pages)
i. Hours of operation
ii. Contact Info
1. Tel
2. Fax
3. Email
4. Address
5. Get directions (link to Google Maps)
2. Our Clinic
a. Main Page
i. Clinic Name
ii. Overview
iii. Languages Spoken
iv. Secondary Navigation
1. Mission
2. Services
3. Clinic Policies
4. Schedules (see attachment)
b. Our Clinic > Mission
c. Our Clinic > Services
i. For each service include service TITLE and DESCRIPTION
d. Our Clinic > Clinic Policies
i. For each policy include policy TITLE and DESCRIPTION
ii. Include the following policies in mockup
1. Late arrivals
2. Missed appointments
3. Fees for missed appointments
4. Referrals and follow-ups
5. Services not covered by RDV
6. Information for TQL patients
7. Medical Legal Reports
e. Our Clinic > Schedules
3. Our Staff
a. Main Page
i. Display a list of staff members. Include NAME and DESIGNATION
b. Our Staff > [Staff Name]
i. Include NAME, PICTURE, DESIGNATION, and BIO
4. Resources
a. Resources > Patient Health
i. Main Page
1. Posts (ordered by date)
a. Title
b. Summary
2. Side Navigation
a. Post Categories
ii. Patient Health > [post title]
1. Title
2. Post Category
3. Date
4. Author
5. Summary
6. Body
b. Resources > Links
1. Secondary Navigation - Categories
a. Sample Categories:
i. Local Services
ii. RDV and Drug Coverage
iii. Mental Health Resources
2. Category page
a. Include the following links in the 'Local Services' category
i. Hypertension clinics
ii. Home Care services
iii. Vaccine Clinics
c. Resources > Forms
i. Display a table with form TITLE and CATEGORY
ii. Side Navigation
1. Form Categories
a. Use the following sample Categories
i. Referrals
ii. Insurance
iii. Intake
iv. Discharge
v. Waivers
5. Alerts
a. Main page
i. List of all Alert posts
1. Include post TITLE as a link to the post
ii. Side Navigation
1. Alerts Archive
a. shown as Month + Number of posts
iii. Alerts > [Alert page]
1. Include TITLE, DATE, AUTHOR, BODY
6. Contact Us
a. Map
b. Hours of operation
c. Address
d. Phone number
e. Fax number
e. Fax number
f. Map
g. Email

Design notes:
- fixed width
- responsive (need designs for mobile, tablet, and desktop)
- simple, dark font, white background
- use Font Awesome icons where needed
- user adds own logo

Target Market(s)

Medical Clinics

Industry/Entity Type

Medical

Number of Pages Required

5+ page

Font styles to use
Serif
Sans Serif

Requirements
Must have
• Please keep designs very simple.
• Examples:
• https://www.quandrix.com/install
• http://www.tervolane.com/company/about-us
• http://brightnumberhub.org/
• http://www.vorn.com/
Should not have
• Minimal or no use of shadows and gradients

```html
<!DOCTYPE html>
<html lang="en">
<head>
<meta charset="utf-8">
<title>Fenwick Clinics</title>
<link rel="stylesheet" href="https://fonts.googleapis.com/css2?family=Raleway:wght@400;500;600;700&family=Open+Sans:wght@400;600&display=swap">
<style>
  :root {
    --blue: #079fe3;
    --blue-soft: #8fd3f4;
    --ink: #333333;
    --ink-soft: #555555;
    --muted: #999999;
    --line: #e3e3e3;
    --card: #e9e9e9;
    --white: #ffffff;
    --hero-tone: #cdd8e4;
    --caption: rgba(105,105,105,0.55);
    --tone-family: #ead9cd;
    --tone-consult: #d8cbc3;
    --tone-lab: #8dbccb;
    --tone-pharmacy: #d5dbe1;
    --tone-doctor: #d3ecf8;
    --tone-michael: #e1d8c6;
    --tone-agnes: #dbe4df;
    --tone-john: #d3dae2;
    --tone-clara: #e3eaf1;
  }
  * { box-sizing: border-box; margin: 0; padding: 0; }
  html, body { width: 1200px; height: 2532px; overflow: hidden; background: var(--white); }
  body { position: relative; font-family: "Raleway", sans-serif; color: var(--ink); }
  .abs { position: absolute; }
  a { color: inherit; text-decoration: none; }

  .brand { left: 98px; top: 44px; font-size: 34px; font-weight: 600; color: var(--blue); letter-spacing: -0.3px; }

  .hero { left: 0; top: 150px; width: 1200px; height: 555px; background: var(--hero-tone); }
  .hero-caption { left: 0; top: 605px; width: 1200px; height: 100px; background: var(--caption); }
  .hero-caption p { position: absolute; left: 101px; top: 22px; color: var(--white); font-weight: 700; font-size: 19px; line-height: 34px; text-transform: uppercase; letter-spacing: 0.2px; }
  .btn-toolbox { left: 707px; top: 633px; width: 231px; height: 44px; background: var(--blue); border: 2px solid var(--blue-soft); color: var(--white);
    font-weight: 700; font-size: 17px; display: flex; align-items: center; justify-content: center; text-transform: uppercase; }
  .dots { left: 1045px; top: 646px; display: flex; gap: 4px; }
  .dots span { width: 17px; height: 17px; border-radius: 50%; border: 2px solid var(--white); }
  .dots span.on { background: var(--blue); }

  .main-nav { left: 98px; top: 120px; width: 1004px; height: 59px; background: var(--blue); display: flex; }
  .main-nav a { flex: 1; display: flex; align-items: center; justify-content: center; color: var(--white); font-weight: 700; font-size: 14px; text-transform: uppercase;
    border-right: 1px solid rgba(255,255,255,0.15); }
  .main-nav a:last-child { border-right: 0; }

  .intro { left: 150px; top: 754px; width: 900px; text-align: center; font-size: 21px; line-height: 33px; color: var(--ink-soft); }

  .gallery-item { top: 879px; width: 226px; height: 220px; border-radius: 22px; border: 6px solid #e6e6e6; }
  .g1 { left: 216px; background: var(--tone-family); }
  .g2 { left: 488px; background: var(--tone-consult); }
  .g3 { left: 758px; background: var(--tone-lab); }
  .arrow { top: 974px; }

  .rule { left: 98px; width: 1004px; height: 1px; background: var(--line); }

  .about { left: 98px; top: 1192px; width: 515px; }
  .about h2 { font-size: 27px; font-weight: 500; color: var(--ink); }
  .about h3 { margin-top: 12px; font-size: 16px; font-weight: 500; color: var(--blue); }
  .about p { margin-top: 22px; font-family: "Open Sans", sans-serif; font-size: 12.5px; line-height: 27px; color: var(--ink-soft); }
  .about p a { color: var(--blue); font-weight: 600; text-decoration: underline; }
  .btn-book { left: 98px; top: 1421px; width: 181px; height: 37px; background: var(--blue); color: var(--white); font-weight: 700; font-size: 13px;
    display: flex; align-items: center; justify-content: center; text-transform: uppercase; }
  .vrule { left: 655px; top: 1202px; width: 1px; height: 250px; background: var(--line); }

  .alerts { left: 712px; top: 1198px; width: 390px; height: 262px; border: 8px solid #e4e4e4; background: var(--white); }
  .alerts h4 { position: absolute; left: 14px; top: 22px; font-size: 18px; font-weight: 500; }
  .alerts ul { position: absolute; left: 14px; top: 70px; list-style: none; }
  .alerts li { display: flex; align-items: center; gap: 8px; font-family: "Open Sans", sans-serif; font-size: 13px; color: var(--ink-soft); height: 31px; }
  .alerts .more { position: absolute; left: 14px; top: 212px; font-size: 13px; font-weight: 600; color: var(--blue); text-decoration: underline; }
  .alerts .photo { position: absolute; left: 188px; top: 1px; width: 186px; height: 244px; background: var(--tone-pharmacy); }

  .banner { left: 98px; top: 1531px; width: 1004px; height: 179px; background: var(--blue); }
  .banner .photo { position: absolute; left: 96px; top: 0; width: 211px; height: 179px; background: var(--tone-doctor); }
  .banner h2 { position: absolute; left: 354px; top: 26px; color: var(--white); font-size: 25px; font-weight: 700; }
  .banner p { position: absolute; left: 354px; top: 73px; width: 560px; color: var(--white); font-family: "Open Sans", sans-serif; font-size: 12.5px; line-height: 25px; }

  .staff-title { left: 98px; top: 1756px; font-size: 27px; font-weight: 500; }
  .staff-card { top: 1825px; width: 213px; height: 290px; background: var(--card); padding: 8px; }
  .staff-card .photo { width: 197px; height: 142px; }
  .staff-card h5 { margin: 12px 0 0 6px; font-size: 16px; font-weight: 600; color: var(--ink); }
  .staff-card .role { margin: 4px 0 0 6px; font-size: 12px; color: var(--blue); font-family: "Open Sans", sans-serif; }
  .staff-card p { margin: 10px 0 0 6px; font-family: "Open Sans", sans-serif; font-size: 12px; line-height: 20px; color: var(--ink-soft); }
  .staff-card .more { display: block; margin: 8px 0 0 6px; font-size: 12px; color: var(--blue); text-decoration: underline; }
  .s1 { left: 98px; } .s2 { left: 361px; } .s3 { left: 625px; } .s4 { left: 888px; }
  .p1 { background: var(--tone-michael); }
  .p2 { background: var(--tone-agnes); }
  .p3 { background: var(--tone-john); }
  .p4 { background: var(--tone-clara); }

  .footer-col h6 { font-size: 15px; font-weight: 600; color: var(--ink); }
  .footer-col ul { list-style: none; margin-top: 20px; }
  .footer-col li { font-family: "Open Sans", sans-serif; font-size: 12px; color: var(--ink-soft); height: 27px; }
  .f1 { left: 98px; top: 2219px; } .f2 { left: 360px; top: 2219px; } .f3 { left: 589px; top: 2219px; } .f4 { left: 903px; top: 2231px; }
  .fdiv { top: 2225px; width: 1px; height: 185px; background: var(--line); }
  .field { width: 201px; height: 34px; border: 1px solid #dcdcdc; font-family: "Open Sans", sans-serif; font-size: 11px; color: var(--muted); padding: 0 8px; display: flex; align-items: center; }
  .form-btn { width: 137px; height: 26px; background: var(--blue); color: var(--white); font-size: 11.5px; font-weight: 600; display: flex; align-items: center; justify-content: center; margin-top: 23px; }
  .contact li { display: flex; align-items: flex-start; gap: 8px; height: auto; line-height: 25px; margin-bottom: 8px; }
  .contact svg { margin-top: 6px; flex: none; }
  .copyright { left: 0; top: 2479px; width: 1200px; text-align: center; font-family: "Open Sans", sans-serif; font-size: 12px; color: var(--ink-soft); }
</style>
</head>
<body>
  <div class="abs brand">Fenwick Clinics</div>

  <div class="abs hero" role="img" aria-label="Photo of a smiling patient with a nurse in blue scrubs behind her"></div>
  <div class="abs hero-caption"><p>Finibus bonorum et malorum righteous indignation<br>saying through shrinking</p></div>
  <a class="abs btn-toolbox" href="#">Physician Toolbox</a>
  <div class="abs dots"><span class="on"></span><span></span><span></span></div>

  <nav class="abs main-nav">
    <a href="#">Home</a><a href="#">Clinic</a><a href="#">Our Staff</a><a href="#">Resources</a><a href="#">Contact Us</a>
  </nav>

  <p class="abs intro">At vero eos et accusamus et iusto odio dignissimos ducimus qui blanditiis praesentium voluptatum deleniti atque corrupti quos dolores</p>

  <svg class="abs arrow" style="left:152px" width="20" height="34" viewBox="0 0 20 34"><path d="M17 3 L4 17 L17 31" fill="none" stroke="#c4c4c4" stroke-width="3"/></svg>
  <div class="abs gallery-item g1" role="img" aria-label="Photo of a doctor examining a child with her mother"></div>
  <div class="abs gallery-item g2" role="img" aria-label="Photo of a doctor talking with an elderly patient"></div>
  <div class="abs gallery-item g3" role="img" aria-label="Photo of a scientist working in a laboratory"></div>
  <svg class="abs arrow" style="left:1027px" width="20" height="34" viewBox="0 0 20 34"><path d="M3 3 L16 17 L3 31" fill="none" stroke="#c4c4c4" stroke-width="3"/></svg>

  <div class="abs rule" style="top:1150px"></div>

  <section class="abs about">
    <h2>A few Word About Us</h2>
    <h3>Omnis voluptas assumenda est omnis dolor repellendus</h3>
    <p>At vero eos et accusamus et iusto odio dignissimos ducimus qui blanditiis praesentium voluptatum deleniti atque corrupti quos dolores et quas molestias excepturi sint occaecati cupiditate non provident, similique sunt in culpa qui officia deserunt mollitia animi, id est laborum et dolorum fuga. <a href="#">Read More</a></p>
  </section>
  <a class="abs btn-book" href="#">Book an Appoinment</a>
  <div class="abs vrule"></div>

  <aside class="abs alerts">
    <h4>Alerts / Bulletins</h4>
    <ul>
      <li><svg width="12" height="10" viewBox="0 0 12 10"><path d="M1 5 L4.5 8.5 L11 1.5" fill="none" stroke="#079fe3" stroke-width="2.4"/></svg>voluptatibus maiores</li>
      <li><svg width="12" height="10" viewBox="0 0 12 10"><path d="M1 5 L4.5 8.5 L11 1.5" fill="none" stroke="#079fe3" stroke-width="2.4"/></svg>voluptatibus maiores</li>
      <li><svg width="12" height="10" viewBox="0 0 12 10"><path d="M1 5 L4.5 8.5 L11 1.5" fill="none" stroke="#079fe3" stroke-width="2.4"/></svg>voluptatibus maiores</li>
      <li><svg width="12" height="10" viewBox="0 0 12 10"><path d="M1 5 L4.5 8.5 L11 1.5" fill="none" stroke="#079fe3" stroke-width="2.4"/></svg>voluptatibus maiores</li>
    </ul>
    <a class="more" href="#">Read More</a>
    <div class="photo" role="img" aria-label="Photo of a smiling doctor in a white coat in a pharmacy"></div>
  </aside>

  <section class="abs banner">
    <div class="photo" role="img" aria-label="Photo of a female doctor with glasses and a stethoscope"></div>
    <h2>Accepting/Not Accepting New patients</h2>
    <p>Sed ut perspiciatis unde omnis iste natus error sit voluptatem accusantium doloremque laudantium, totam rem aperiam, eaque ipsa quae.</p>
  </section>

  <h2 class="abs staff-title">Our Staff</h2>
  <article class="abs staff-card s1">
    <div class="photo p1" role="img" aria-label="Photo of staff member Michael"></div>
    <h5>Michael</h5><div class="role">Optometrist</div>
    <p>At vero eos et accusamus et<br>iusto odio dignissimos .</p><a class="more" href="#">Read More</a>
  </article>
  <article class="abs staff-card s2">
    <div class="photo p2" role="img" aria-label="Photo of staff member Agnes"></div>
    <h5>Agnes</h5><div class="role">Optometrist</div>
    <p>At vero eos et accusamus et<br>iusto odio dignissimos .</p><a class="more" href="#">Read More</a>
  </article>
  <article class="abs staff-card s3">
    <div class="photo p3" role="img" aria-label="Photo of staff member John"></div>
    <h5>John</h5><div class="role">Optometrist</div>
    <p>At vero eos et accusamus et<br>iusto odio dignissimos .</p><a class="more" href="#">Read More</a>
  </article>
  <article class="abs staff-card s4">
    <div class="photo p4" role="img" aria-label="Photo of staff member Clara"></div>
    <h5>Clara</h5><div class="role">Optometrist</div>
    <p>At vero eos et accusamus et<br>iusto odio dignissimos .</p><a class="more" href="#">Read More</a>
  </article>

  <div class="abs rule" style="top:2174px; left:0; width:1200px"></div>

  <div class="abs footer-col f1"><h6>Information</h6>
    <ul><li>About Us</li><li>Client Care</li><li>Special Services</li><li>Monthly Medical Services</li></ul></div>
  <div class="abs fdiv" style="left:294px"></div>
  <div class="abs footer-col f2"><h6>Quick Links</h6>
    <ul><li>Blog</li><li>Skin Care</li><li>Legal Disclaimer</li><li>Contact</li></ul></div>
  <div class="abs fdiv" style="left:522px"></div>
  <div class="abs footer-col f3"><h6>Appoinment</h6>
    <div class="field" style="margin-top:29px">Name :</div>
    <div class="field" style="margin-top:20px">Email :</div>
    <div class="form-btn">Book An Appoinment</div></div>
  <div class="abs fdiv" style="left:846px"></div>
  <div class="abs footer-col f4 contact"><h6>Contact Us</h6>
    <ul>
      <li><svg width="10" height="14" viewBox="0 0 10 14"><path d="M5 0 C2.2 0 0 2.2 0 5 C0 8.5 5 14 5 14 C5 14 10 8.5 10 5 C10 2.2 7.8 0 5 0 Z M5 7 A2 2 0 1 1 5 3 A2 2 0 1 1 5 7 Z" fill="#079fe3"/></svg><span>1420 Alder Lane, Northvale,<br>K7 3PL +1(555) 010-2040</span></li>
      <li><svg width="13" height="13" viewBox="0 0 13 13"><path d="M3 0.5 L5 3.5 L3.6 5 C4.5 7 6 8.5 8 9.4 L9.5 8 L12.5 10 L11 12.5 C5.5 12 1 7.5 0.5 2 Z" fill="#079fe3"/></svg><span>1-555-010-7788</span></li>
      <li><svg width="13" height="13" viewBox="0 0 13 13"><circle cx="6.5" cy="6.5" r="6.5" fill="#079fe3"/><path d="M0.5 6.5 H12.5 M6.5 0.5 C3.5 4 3.5 9 6.5 12.5 M6.5 0.5 C9.5 4 9.5 9 6.5 12.5" fill="none" stroke="#fff" stroke-width="1"/></svg><span>www.fenwickclinic.example</span></li>
    </ul></div>

  <div class="abs rule" style="top:2448px"></div>
  <p class="abs copyright">Fenwick Clinic © 2015 All Rights Reserved &nbsp;|&nbsp; Privacy Policy</p>
</body>
</html>
```